Brookside Grocer

Hope all is well!

Wanted to make business cards for my father. His name is Faisal Qureshi and owns convenience stores. I have attached logo :)

He does not want any title just simple name and phone. An email would be nice as well.

Faisal Qureshi
Cell: 413-585-2046
Store: 413-719-4820

Brooksidegrocer512@fernpost.com

The design and style is totally up to you :) The colors we were looking for were the same as logo :)

```html
<!DOCTYPE html>
<html lang="en">
<head>
<meta charset="utf-8">
<title>Brookside Grocer – Business Cards</title>
<link rel="stylesheet" href="https://fonts.googleapis.com/css2?family=Montserrat:wght@400;500;700&display=swap">
<style>
  :root {
    --backdrop: #1c1c1e;
    --card-navy: #213478;
    --card-navy-light: #2a3f8a;
    --accent-red: #e8363d;
    --ink-white: #ffffff;
  }
  * { box-sizing: border-box; margin: 0; padding: 0; }
  html, body {
    width: 1200px;
    height: 801px;
    overflow: hidden;
    background: var(--backdrop);
    font-family: "Montserrat", sans-serif;
  }
  .stage {
    position: relative;
    width: 1200px;
    height: 801px;
    display: flex;
    align-items: center;
    justify-content: center;
    gap: 40px;
  }
  .card {
    position: relative;
    width: 525px;
    height: 300px;
    background: linear-gradient(135deg, var(--card-navy) 0%, var(--card-navy-light) 55%, var(--card-navy) 100%);
    border: 3px solid var(--accent-red);
    color: var(--ink-white);
    overflow: hidden;
  }

  /* Brand name */
  .brand {
    display: flex;
    align-items: center;
    gap: 10px;
    color: var(--ink-white);
    font-weight: 700;
    text-transform: uppercase;
    white-space: nowrap;
  }
  .brand-mark {
    flex: none;
    background: var(--accent-red);
  }

  /* Contact side */
  .card-contact .brand {
    position: absolute;
    top: 58px;
    right: 46px;
    font-size: 22px;
    letter-spacing: 1px;
  }
  .card-contact .brand-mark { width: 14px; height: 14px; }

  .holder {
    position: absolute;
    left: 40px;
    bottom: 40px;
  }
  .holder-name {
    color: var(--accent-red);
    font-weight: 700;
    font-size: 21px;
    letter-spacing: 1px;
    text-transform: uppercase;
  }
  .holder-rule {
    width: 12px;
    height: 2px;
    background: var(--accent-red);
    margin: 12px 0 10px;
  }
  .contact-list { list-style: none; }
  .contact-list li {
    display: flex;
    align-items: center;
    gap: 9px;
    font-size: 13.5px;
    font-weight: 400;
    line-height: 22px;
    letter-spacing: 0.3px;
  }
  .contact-list .label {
    font-size: 10px;
    margin-left: 4px;
  }
  .contact-icon { width: 12px; height: 12px; flex: none; }

  /* Brand side */
  .card-brand {
    display: flex;
    align-items: center;
    justify-content: center;
  }
  .card-brand .brand {
    font-size: 34px;
    letter-spacing: 1.5px;
    gap: 14px;
  }
  .card-brand .brand-mark { width: 22px; height: 22px; }
</style>
</head>
<body>
<main class="stage">

  <section class="card card-contact" aria-label="Business card, contact side">
    <div class="brand">
      <span class="brand-mark"></span>
      <span class="brand-name">Brookside Grocer</span>
    </div>

    <div class="holder">
      <h1 class="holder-name">Faisal Qureshi</h1>
      <div class="holder-rule"></div>
      <ul class="contact-list">
        <li>
          <svg class="contact-icon" viewBox="0 0 24 24" aria-hidden="true">
            <path fill="#e8363d" d="M6.6 10.8a15.1 15.1 0 0 0 6.6 6.6l2.2-2.2a1 1 0 0 1 1-.25 11.4 11.4 0 0 0 3.6.57 1 1 0 0 1 1 1V20a1 1 0 0 1-1 1A17 17 0 0 1 3 4a1 1 0 0 1 1-1h3.5a1 1 0 0 1 1 1c0 1.25.2 2.45.57 3.57a1 1 0 0 1-.25 1z"/>
          </svg>
          <span>413-585-2046<span class="label">(Cell)</span></span>
        </li>
        <li>
          <svg class="contact-icon" viewBox="0 0 24 24" aria-hidden="true">
            <path fill="#e8363d" d="M3 8c0-2 4-4 9-4s9 2 9 4v2h-5V8.5c-1.2-.4-2.6-.5-4-.5s-2.8.1-4 .5V10H3zM6 12h12l2 8H4zm6 2a2.5 2.5 0 1 0 0 5 2.5 2.5 0 0 0 0-5z"/>
          </svg>
          <span>413-719-4820<span class="label">(Store)</span></span>
        </li>
        <li>
          <svg class="contact-icon" viewBox="0 0 24 24" aria-hidden="true">
            <path fill="#e8363d" d="M2 6h20v12H2zm2 2v.4l8 5 8-5V8l-8 5z"/>
          </svg>
          <span>Brooksidegrocer512@fernpost.com</span>
        </li>
      </ul>
    </div>
  </section>

  <section class="card card-brand" aria-label="Business card, brand side">
    <div class="brand">
      <span class="brand-mark"></span>
      <span class="brand-name">Brookside Grocer</span>
    </div>
  </section>

</main>
</body>
</html>
```